Pathways to Brightmoor Land Ventures

size of the ad - 8”x 10.75" plus 0.25" bleed
I would like an ad for a magazine that will stand out and make people want to read the ad.
The ad should not be crowded and people reading the ad will be able to read the text.
I would like it to be a creative and modern-day design.
the list of topics should not be the focus of the ad.
the text is attached.
If you decide to use people in the ad then please no ladies.
please note that leave over 1 inch for the bottom of the footer

```html
<!DOCTYPE html>
<html lang="en">
<head>
<meta charset="utf-8">
<title>Real Estate Course – Pathways to Brightmoor Land Ventures</title>
<link href="https://fonts.googleapis.com/css2?family=Anton&family=Montserrat:ital,wght@0,600;0,700;0,800;1,600&family=Roboto+Slab:wght@800&display=swap" rel="stylesheet">
<style>
:root{
  --navy:#1d2660;
  --navy-deep:#141a45;
  --yellow:#ffe500;
  --gold:#f5b400;
  --red:#d8222a;
  --white:#ffffff;
  --ink:#1c2253;
}
*{margin:0;padding:0;box-sizing:border-box}
html,body{width:907px;height:1200px;overflow:hidden;background:#fff}
.ad{position:relative;width:907px;height:1200px;overflow:hidden;font-family:'Montserrat',sans-serif;color:var(--white)}
.hero-photo{position:absolute;inset:0;
  background:
   linear-gradient(180deg,rgba(20,26,69,0) 0%,rgba(20,26,69,0) 44%,rgba(20,26,69,.55) 55%,rgba(20,26,69,.75) 100%),
   linear-gradient(180deg,#8fa0d8 0%,#b7a9d6 14%,#d9b3c8 22%,#5a6686 34%,#6f7a92 44%,#3c4258 52%,#4a4a58 62%,#5b5248 78%,#2a2d45 100%);}
.quote{position:absolute;left:59px;top:59px;width:237px;height:163px;border:2px solid var(--red);background:rgba(255,255,255,.88);
  display:flex;align-items:center;justify-content:center;text-align:center;
  font-family:'Roboto Slab',serif;font-weight:800;font-size:25px;line-height:1.2;color:var(--ink)}
.quote-mark{position:absolute;font-family:'Roboto Slab',serif;font-weight:800;font-size:86px;color:var(--red);line-height:1}
.quote-mark.open{left:-4px;top:-22px}
.quote-mark.close{right:-6px;bottom:-58px}
.title-band{position:absolute;left:0;top:530px;width:907px;height:170px;background:linear-gradient(180deg,rgba(29,38,96,.82),rgba(29,38,96,.92))}
.title{position:absolute;left:0;width:907px;top:538px;text-align:center;font-family:'Anton',sans-serif;font-size:104px;line-height:1.05;color:var(--yellow);letter-spacing:1px;transform:scaleY(1.12)}
.subtitle{position:absolute;left:0;width:907px;top:646px;text-align:center;font-weight:700;font-size:29px;letter-spacing:.5px;text-transform:uppercase}
.tab{position:absolute;left:0;width:500px;height:50px}
.tab-label{position:absolute;left:50px;top:0;line-height:50px;font-size:34px;font-weight:700}
.tab-label b{font-weight:800}
.tab-label span{font-weight:600}
.tab.location{top:706px}
.tab.topics{top:873px}
.details{position:absolute;left:70px;top:765px;font-weight:700;font-size:21px;line-height:33px}
.offer{position:absolute;left:508px;top:753px;width:331px;height:99px;border:3px solid var(--gold);padding:10px 0 0 26px;
  font-style:italic;font-weight:600;font-size:15.5px;line-height:22px}
.offer li{list-style:none;position:relative;padding-left:14px;margin-bottom:8px}
.offer svg{position:absolute;left:-22px;top:-2px}
.topic-list{position:absolute;top:936px;list-style:none;font-weight:600;font-size:21px;line-height:32.5px}
.topic-list li{position:relative;padding-left:28px}
.topic-list li::before{content:"";position:absolute;left:2px;top:11px;width:11px;height:11px;border-radius:50%;background:var(--gold)}
.topic-list.left{left:72px}
.topic-list.right{left:486px}
.footer{position:absolute;left:0;bottom:0;width:907px;height:200px}
</style>
</head>
<body>
<div class="ad">
  <div class="hero-photo" role="img" aria-label="Photo of a two-storey grey family house with lit windows and a triple garage at dusk, blurred and darkened toward the bottom"></div>

  <div class="quote">
    <span class="quote-mark open">“</span>
    <p>Investing In<br>Knowledge<br>Is Investing In<br>Opportunities.</p>
    <span class="quote-mark close">”</span>
  </div>

  <div class="title-band"></div>
  <h1 class="title">REAL ESTATE COURSE</h1>
  <p class="subtitle">Pathways to Brightmoor Land Ventures</p>

  <div class="tab location">
    <svg width="500" height="50" viewBox="0 0 500 50"><polygon points="0,0 455,0 425,50 0,50" fill="var(--navy)"/><polygon points="462,0 500,0 470,50 432,50" fill="var(--gold)"/></svg>
    <div class="tab-label"><b>Westvale</b></div>
  </div>

  <div class="details">
    <p>10 -Tuesday evenings sessions</p>
    <p>Starting Feb.28</p>
    <p>Limited Partial Scholarships</p>
  </div>

  <ul class="offer">
    <li><svg width="26" height="24" viewBox="0 0 26 24"><path d="M3 13 L10 20 L24 3" fill="none" stroke="var(--red)" stroke-width="4" stroke-linecap="round" stroke-linejoin="round"/></svg>Early Bird Special</li>
    <li><svg width="26" height="24" viewBox="0 0 26 24"><path d="M3 13 L10 20 L24 3" fill="none" stroke="var(--red)" stroke-width="4" stroke-linecap="round" stroke-linejoin="round"/></svg>For those that started or would like to go into real estate</li>
  </ul>

  <div class="tab topics">
    <svg width="500" height="50" viewBox="0 0 500 50"><polygon points="0,0 455,0 425,50 0,50" fill="var(--navy)"/><polygon points="462,0 500,0 470,50 432,50" fill="var(--gold)"/></svg>
    <div class="tab-label"><b>Topics:</b> <span>partial listing</span></div>
  </div>

  <ul class="topic-list left">
    <li>Real estate investment strategies</li>
    <li>Due diligence</li>
    <li>Financing</li>
    <li>Underwriting</li>
    <li>Property management</li>
  </ul>
  <ul class="topic-list right">
    <li>Real estate Legal basics</li>
    <li>Sourcing deals</li>
    <li>Syndication</li>
    <li>Dealing with brokers</li>
    <li>Tax fundamentals</li>
  </ul>

  <svg class="footer" viewBox="0 0 907 200" preserveAspectRatio="none">
    <rect x="0" y="100" width="907" height="100" fill="var(--navy)"/>
    <polygon points="0,170 907,170 907,200 0,200" fill="var(--white)"/>
    <polygon points="560,200 907,40 907,72 640,200" fill="var(--gold)"/>
    <polygon points="650,200 907,82 907,104 700,200" fill="var(--white)"/>
    <polygon points="720,200 907,114 907,140 780,200" fill="var(--navy-deep)"/>
    <polygon points="600,185 907,30 907,40 620,185" fill="var(--yellow)"/>
  </svg>
</div>
</body>
</html>
```